Elegant, High End Integrated Wellness Healthcare Practice

We need a brochure designed for an integrated mind-body wellness healthcare practice (www.larchveilclinic.com) . This brochure will be used when we cold call prospects (physicians to refer to our office, and potential consumers to utilize our services). Our practice is geographically located in the middle Tennessee USA region, although we have plans to become an international company as many of our offerings can be accessed anywhere in the world. Ultimately our goal is to have this brochure used as a leave-behind in an effort to introduce our integrated offerings to increase market share. The final product brochure should be both elegant and serious, with clean lines but also convey warmth and trust, as individuals who are coming for our services have usually struggled with their health for a significant amount of time before finding our practice.

The design brief was very specific about providing a high-end science-based 2-page brochure (not flier). Several designs submitted were fliers. The other designs were heavy on yoga or "woo woo" non-science-based looking pictures. This is a flier to appeal to physicians and other healthcare providers. Therefore the design must speak science and evidence-based methods of mind and body wellness care. I would also like to appeal to the other designers I paid extra for their submissions and who have indicated they will "respond in the coming days."

```html
<!DOCTYPE html>
<html lang="en">
<head>
<meta charset="utf-8">
<title>Larchveil Clinic Brochure</title>
<link rel="stylesheet" href="https://fonts.googleapis.com/css2?family=Montserrat:wght@300;400;500&display=swap">
<style>
  :root{
    --green:#6a9c3c;
    --green-soft:#d8e0c7;
    --ring-pale:#e9edd8;
    --charcoal:#555657;
    --ink:#3a3a3a;
    --paper:#ffffff;
    --paper-gray:#eeeeee;
    --stage:#e4e4e4;
  }
  *{box-sizing:border-box;margin:0;padding:0}
  html,body{width:1200px;height:900px;overflow:hidden}
  body{background:var(--stage);font-family:"Montserrat",Arial,sans-serif;color:var(--ink);position:relative}
  .spread{position:absolute;left:200px;width:800px;height:400px;display:flex;box-shadow:0 6px 14px rgba(0,0,0,.12)}
  .spread--outer{top:40px}
  .spread--inner{top:460px}
  .page{position:relative;width:400px;height:400px;overflow:hidden;background:var(--paper)}

  .brand{display:flex;align-items:center;gap:6px;color:var(--green);font-weight:500;font-size:12px;white-space:nowrap}
  .brand__dot{width:20px;height:20px;border-radius:50%;background:var(--green);flex:none}

  /* back cover */
  .contact-ring{position:absolute;left:90px;top:68px;width:216px;height:216px;border:3px solid var(--ring-pale);border-radius:50%;
    display:flex;flex-direction:column;align-items:center;justify-content:center;text-align:center;font-size:9px;line-height:1.3;padding:0 28px}
  .contact-ring .brand{margin-bottom:14px}
  .contact-ring p{margin-bottom:7px}
  .site{position:absolute;left:0;right:0;top:340px;text-align:center;color:var(--green);font-size:13px;letter-spacing:1.2px}

  /* front cover */
  .page--cover{background:linear-gradient(135deg,#f4f4f4,#e6e6e6)}
  .cover-shapes{position:absolute;inset:0}
  .cover-title{position:absolute;left:24px;top:28px;font-weight:300;font-size:23px;line-height:28px;color:var(--ink)}
  .cover-rule{position:absolute;left:24px;top:118px;width:160px;height:1px;background:var(--green)}
  .page--cover .brand{position:absolute;left:283px;top:22px;font-size:10px}
  .page--cover .brand__dot{width:18px;height:18px}
  .location-badge{position:absolute;left:27px;top:150px;width:96px;height:96px;border-radius:50%;background:var(--green);color:#f2f5ea;
    display:flex;align-items:center;justify-content:center;text-align:center;font-size:11px;line-height:17px}
  .portrait-ring{position:absolute;left:178px;top:70px;width:210px;height:210px;border-radius:50%;background:var(--green);border:4px solid #dfe3d6}
  .portrait{position:absolute;left:8px;top:8px;width:186px;height:186px;border-radius:50%;background:radial-gradient(circle at 50% 40%,#d9d2c6,#8d8c8a)}
  .tagline{position:absolute;left:22px;top:322px;color:#eeeeee;font-weight:300;font-size:14px;line-height:21px}
  .call{position:absolute;right:22px;top:356px;text-align:right;color:#fff;line-height:1}
  .call__label{font-size:12px}
  .call__number{font-size:19px;margin-top:3px}

  /* inner left */
  .page--package{background:linear-gradient(90deg,#ffffff,#f2f2f2)}
  .package-title{position:absolute;left:28px;top:38px;width:280px;color:var(--green);font-weight:400;font-size:16.5px;line-height:20px;text-transform:uppercase}
  .package-body{position:absolute;left:28px;top:116px;width:226px;font-size:9.8px;line-height:14.2px}
  .model-photo{position:absolute;left:266px;top:34px;width:118px;height:220px;background:linear-gradient(180deg,#ebebeb 0%,#a9a9ab 35%,#9a9a9c 80%,#cbbfa8 100%);border-radius:2px}
  .package-note{position:absolute;left:18px;top:254px;width:369px;height:122px;background:var(--green-soft);border-radius:8px;padding:14px 25px;font-size:9.6px;line-height:14px;text-align:justify}
  .package-note p+p{margin-top:6px}

  /* inner right */
  .page--story{background:linear-gradient(180deg,#f7f8f5,#ffffff)}
  .story{position:absolute;left:45px;top:26px;width:318px;font-size:7.6px;line-height:9.9px}
  .story p+p{margin-top:8px}
  .scene-photo{position:absolute;left:0;top:200px;width:400px;height:200px;background:linear-gradient(180deg,rgba(255,255,255,1) 0%,#e8ebe4 35%,#8fa27a 72%,#b7bdb3 100%)}
  .page--story .brand{position:absolute;left:253px;top:280px;font-size:10.5px}
</style>
</head>
<body>

<section class="spread spread--outer">
  <article class="page page--back">
    <div class="contact-ring">
      <div class="brand"><span class="brand__dot"></span>Larchveil Clinic</div>
      <p>418 Alder Ridge Rd.<br>Murfreesboro, TN 37128.</p>
      <p>Office Hours: Monday - Friday: 8 am - 7 pm</p>
      <p>Call Now: (615) 555-0142</p>
    </div>
    <div class="site">www.larchveilclinic.com</div>
  </article>

  <article class="page page--cover">
    <svg class="cover-shapes" viewBox="0 0 400 400" width="400" height="400" aria-hidden="true">
      <polygon points="0,283 194,220 194,226 0,292" fill="#d9dccd"/>
      <polygon points="0,292 194,226 194,240 0,322" fill="var(--green)"/>
      <polygon points="0,322 194,240 400,248 400,400 0,400" fill="var(--charcoal)"/>
      <polygon points="117,400 322,325 400,368 400,400" fill="var(--green)" stroke="#ffffff" stroke-width="2"/>
    </svg>
    <h1 class="cover-title">Discover A<br>Better Way To<br>A Better You</h1>
    <div class="cover-rule"></div>
    <div class="brand"><span class="brand__dot"></span>Larchveil Clinic</div>
    <div class="location-badge">Located in<br>Mufreesboro,<br>TN</div>
    <div class="portrait-ring">
      <div class="portrait" role="img" aria-label="Photo of a relaxed woman holding a mug on a sofa"></div>
    </div>
    <p class="tagline">Integrative<br>healing-oriented care</p>
    <div class="call">
      <div class="call__label">CALL US:</div>
      <div class="call__number">(615) 555-0142</div>
    </div>
  </article>
</section>

<section class="spread spread--inner">
  <article class="page page--package">
    <h2 class="package-title">Wellness Package at Larchveil Clinic in Murfreesboro, TN</h2>
    <p class="package-body">At Larchveil Clinic we facilitate body and mind health and wellness through an integrated functional approach to care. This method of personalized care appreciates you as a unique individual with distinct health circumstances. We tailor our body and mind approaches to address your specific health concerns.</p>
    <div class="model-photo" role="img" aria-label="Photo of a thoughtful man in a gray sweater"></div>
    <div class="package-note">
      <p>Larchveil Clinic offers a unique wellness package you won’t find anywhere else, a combination of a body and mind system designed to “Reunite” your brain and your gut! Contcct us today for more information.</p>
      <p>We are conveniently located at 418 Alder Ridge Rd. Murfreesboro, TN 37128.</p>
    </div>
  </article>

  <article class="page page--story">
    <div class="story">
      <p>Dr. Nora Hale has been a practicing clinical psychologist for 15+ years. Through her time working with people who are stressed, anxious, angry, and depressed she has seen first-hand that medication and psychotherapy are often not enough to make true change. What has been missing is body change - one's body has to change for the mind to integrate other parts of a person's approach to life and make them part of the person.</p>
      <p>It seems like the concept of body-mind would be a "no-brainer"—that if your body is in harmony with your mind then you will feel good- or at least better- in the body, you are in. Unfortunately, the way current health practices operate is one of the silos, and little crossover between traditional medicine and alternative therapies. If someone feels stressed out, anxious, irritable, unable to focus, or just plain unhappy many traditional medical practitioners will look to prescriptions to help with these symptoms. Treating symptoms may help someone to feel better in the short run but does not "fix" an underlying issue that may be driving the feelings.</p>
    </div>
    <div class="scene-photo" role="img" aria-label="Photo of a woman breathing fresh air by a lake"></div>
    <div class="brand"><span class="brand__dot"></span>Larchveil Clinic</div>
  </article>
</section>

</body>
</html>
```